Whitmore Business Card Design

The name of the business is Dara Whitmore, CPA LLC
The service that we offer is Accounting, Tax & Consulting Services. I need it to have the following items:
Dara Whitmore, Principal
Phone Number
Email Address
Physical Address

I have attached the company logo, one in black and one in white. Please provide a design in black background and the other in white background. Please include "Accounting, Tax & Consulting Services". I want the business card to be clean and very professional.

```html
<!DOCTYPE html>
<html lang="en">
<head>
<meta charset="utf-8">
<title>Dara Whitmore, CPA LLC — Business Card</title>
<link href="https://fonts.googleapis.com/css2?family=Poppins:wght@400;500;600&display=swap" rel="stylesheet">
<style>
  :root {
    --bg: #2a2a2c;
    --black: #0a0a0a;
    --red: #9c161b;
    --red-light: #b0161c;
    --white: #ffffff;
    --grey: #8c8c8c;
  }
  * { box-sizing: border-box; margin: 0; padding: 0; }
  html, body {
    width: 1200px; height: 1015px; overflow: hidden;
    background: var(--bg);
    font-family: "Poppins", sans-serif;
  }
  .card {
    position: absolute; left: 250px;
    width: 700px; height: 400px;
    overflow: hidden;
    box-shadow: 0 12px 30px rgba(0,0,0,.5);
  }
  .card--front { top: 60px; background: var(--black); }
  .card--back { top: 555px; background: var(--red); }

  .brand { display: flex; align-items: center; gap: 14px; }
  .brand__mark { width: 22px; height: 22px; background: var(--red); flex: none; }
  .brand__name { color: var(--white); font-weight: 600; font-size: 34px; letter-spacing: .5px; line-height: 1.1; }
  .brand__tag { color: var(--grey); font-weight: 500; font-size: 19px; letter-spacing: 4px; margin-top: 6px; }

  .card--front .brand-block { position: absolute; left: 0; right: 0; top: 120px; text-align: center; }
  .card--front .brand { justify-content: center; }

  .band {
    position: absolute; left: 0; right: 0; bottom: 0; height: 72px;
    display: flex; align-items: center; justify-content: center;
    color: var(--white); font-weight: 500; font-size: 20px; letter-spacing: 1px; text-transform: uppercase;
  }
  .card--front .band { background: var(--red); }
  .card--back .band { background: var(--black); }

  .card--back .brand-block { position: absolute; left: 48px; top: 60px; }
  .card--back .brand__mark { background: var(--white); width: 18px; height: 18px; }
  .card--back .brand__name { font-size: 26px; }
  .card--back .brand__tag { color: var(--white); font-size: 14px; letter-spacing: 2.5px; }

  .contacts { position: absolute; left: 48px; top: 172px; color: var(--white); font-size: 17px; line-height: 1.45; }
  .contact { display: flex; align-items: center; gap: 12px; }
  .contact svg { width: 20px; height: 20px; flex: none; }
  .address { margin-top: 14px; padding-left: 32px; }

  .person { position: absolute; right: 56px; top: 90px; color: var(--white); }
  .person__name { font-weight: 600; font-size: 27px; }
  .person__role { font-size: 19px; }

  .accent { position: absolute; background: var(--red-light); opacity: .55; }
  .accent--a { right: 0; top: 0; width: 300px; height: 230px; }
</style>
</head>
<body>
  <section class="card card--front">
    <div class="brand-block">
      <div class="brand">
        <span class="brand__mark"></span>
        <span class="brand__name">Dara Whitmore, CPA LLC</span>
      </div>
      <div class="brand__tag">CERTIFIED PUBLIC ACCOUNTANT</div>
    </div>
    <div class="band">Accounting, Tax &amp; Consulting Services</div>
  </section>

  <section class="card card--back">
    <div class="accent accent--a"></div>
    <div class="brand-block">
      <div class="brand">
        <span class="brand__mark"></span>
        <span class="brand__name">Dara Whitmore, CPA LLC</span>
      </div>
      <div class="brand__tag">CERTIFIED PUBLIC ACCOUNTANT</div>
    </div>

    <div class="person">
      <div class="person__name">Dara Whitmore</div>
      <div class="person__role">Principal</div>
    </div>

    <div class="contacts">
      <div class="contact">
        <svg viewBox="0 0 20 20" fill="none" stroke="#fff" stroke-width="1.6"><rect x="1" y="1" width="18" height="18" rx="2"/><path d="M6 5c0 5 4 9 9 9l0-2.5-2.5-1-1 1.2c-1.5-.6-2.6-1.7-3.2-3.2l1.2-1-1-2.5z" fill="#fff" stroke="none"/></svg>
        <span>044-555 210 387</span>
      </div>
      <div class="contact">
        <svg viewBox="0 0 20 20" fill="none" stroke="#fff" stroke-width="1.6"><rect x="1" y="4" width="18" height="12"/><path d="M1 4l9 7 9-7"/></svg>
        <span>info@whitmorecpa.com</span>
      </div>
      <div class="address">421, Address line here<br>Country Name, 45452</div>
    </div>

    <div class="band">Accounting, Tax &amp; Consulting Services</div>
  </section>
</body>
</html>
```